Business Card and Stationary for Electrical Contractor
Vantor Electric
Business Card and Stationary for Electrical Contractor - Construction
Creative Brief
Professional
Dalton Pryce
Service Technician
1875 Birchwood Lane Kansas City, KS 66109
dpryce@vantorelectricmo.com
www.vantorelectricmo.com

```html
<!DOCTYPE html>
<html lang="en">
<head>
<meta charset="utf-8">
<title>Vantor Electric – Business Card</title>
<link rel="stylesheet" href="https://fonts.googleapis.com/css2?family=Arimo:ital,wght@0,400;0,700;1,400&display=swap">
<style>
  :root {
    --page-bg: #e4e4e2;
    --card-white: #fbfbfa;
    --card-black: #1c1c1d;
    --brand-red: #7a1c1f;
    --brand-red-bright: #9c2328;
    --ink: #2a2a2a;
    --ink-soft: #5b5b5b;
  }
  * { box-sizing: border-box; margin: 0; padding: 0; }
  html, body { width: 1200px; height: 901px; overflow: hidden; }
  body {
    background: var(--page-bg);
    font-family: "Arimo", Arial, sans-serif;
    position: relative;
  }
  .card {
    position: absolute;
    left: 320px;
    width: 560px;
    height: 320px;
    border-radius: 18px;
    overflow: hidden;
  }
  .card-back { top: 90px; background: var(--card-black); display: flex; align-items: center; justify-content: center; }
  .card-front { top: 470px; background: var(--card-white); }

  .back-brand { display: flex; align-items: center; gap: 14px; }
  .brand-square { width: 22px; height: 22px; background: var(--brand-red-bright); }
  .back-brand .brand-name {
    color: #ffffff; font-weight: 700; font-size: 30px; letter-spacing: 3px; text-transform: uppercase;
  }

  .front-brand {
    position: absolute; right: 34px; top: 96px;
    display: flex; align-items: center; gap: 10px;
  }
  .front-brand .brand-square { width: 18px; height: 18px; }
  .front-brand .brand-name {
    color: var(--ink); font-weight: 700; font-size: 22px; letter-spacing: 2px; text-transform: uppercase;
  }

  .person { position: absolute; left: 34px; top: 138px; }
  .person-name { color: var(--brand-red); font-weight: 700; font-size: 22px; text-transform: uppercase; letter-spacing: 0.5px; }
  .person-title { color: var(--ink-soft); font-size: 13px; margin-top: 3px; }

  .divider { position: absolute; left: 34px; right: 34px; top: 188px; height: 1.5px; background: var(--brand-red); }

  .contacts { position: absolute; left: 34px; top: 202px; list-style: none; }
  .contacts li { display: flex; align-items: center; gap: 9px; font-size: 13px; color: var(--ink-soft); height: 21px; }
  .contacts svg { width: 11px; height: 11px; fill: var(--brand-red); }

  .address { position: absolute; right: 34px; top: 204px; text-align: right; font-size: 14px; color: var(--ink); line-height: 19px; }
  .website { color: var(--brand-red); font-weight: 700; letter-spacing: 0.5px; }

  .corner-tab {
    position: absolute; right: 24px; bottom: 0; width: 120px; height: 9px;
    background: var(--brand-red); border-radius: 8px 8px 0 0;
  }
</style>
</head>
<body>
  <section class="card card-back">
    <div class="back-brand">
      <span class="brand-square"></span>
      <span class="brand-name">Vantor Electric</span>
    </div>
  </section>

  <section class="card card-front">
    <div class="front-brand">
      <span class="brand-square"></span>
      <span class="brand-name">Vantor Electric</span>
    </div>

    <div class="person">
      <h1 class="person-name">Dalton Pryce</h1>
      <p class="person-title">Service Technician</p>
    </div>

    <div class="divider"></div>

    <ul class="contacts">
      <li>
        <svg viewBox="0 0 24 24" aria-hidden="true"><path d="M6.6 10.8a15.1 15.1 0 0 0 6.6 6.6l2.2-2.2a1 1 0 0 1 1-.25 11.4 11.4 0 0 0 3.6.57 1 1 0 0 1 1 1V20a1 1 0 0 1-1 1A17 17 0 0 1 3 4a1 1 0 0 1 1-1h3.5a1 1 0 0 1 1 1c0 1.25.2 2.45.57 3.57a1 1 0 0 1-.25 1z"/></svg>
        913-555-0142
      </li>
      <li>
        <svg viewBox="0 0 24 24" aria-hidden="true"><path d="M7 1h10a2 2 0 0 1 2 2v18a2 2 0 0 1-2 2H7a2 2 0 0 1-2-2V3a2 2 0 0 1 2-2zm0 3v14h10V4zm5 15.5a1 1 0 1 0 0 2 1 1 0 0 0 0-2z"/></svg>
        816-555-0178
      </li>
      <li>
        <svg viewBox="0 0 24 24" aria-hidden="true"><path d="M2 5h20v14H2zm2 2v.5l8 5 8-5V7l-8 5z"/></svg>
        dpryce@vantorelectricmo.com
      </li>
    </ul>

    <address class="address" style="font-style: normal;">
      1875 Birchwood Lane<br>
      Kansas City, KS 66109<br>
      <span class="website">vantorelectricmo.com</span>
    </address>

    <div class="corner-tab"></div>
  </section>
</body>
</html>
```